Brindle Hub is an online marketing platform

A daily deals site for consumers a way to bring in new clients for clients and this is who the business cards are for. Industries - Food and Drink, Things To Do, Beauty and Spas, Staycations and Services.This leaflet is going to be used to get member of the public to sign up to our website

```html
<!DOCTYPE html>
<html lang="en">
<head>
<meta charset="utf-8">
<title>Brindle Hub – Launch Leaflet</title>
<link href="https://fonts.googleapis.com/css2?family=Kaushan+Script&family=Tinos:wght@400;700&display=swap" rel="stylesheet">
<style>
  :root{
    --backdrop:#a9a9a9;
    --ink:#0a0a0a;
    --paper:#ffffff;
    --sun:#f6ec4f;
    --sun-pale:#fbf6c0;
    --text-light:#ffffff;
    --text-dark:#141414;
    --rule:#9a9a9a;
    --dine-warm:#b9a07e;
    --dine-green:#8f9a63;
    --spa-soft:#e8dcd2;
  }
  html,body{margin:0;padding:0;width:1200px;height:1200px;overflow:hidden;background:var(--backdrop);}
  .leaflet{position:absolute;left:190px;top:20px;width:820px;height:1160px;background:var(--ink);overflow:hidden;font-family:"Tinos",serif;}
  .hero{position:absolute;left:0;top:0;width:820px;height:440px;}
  .brand{position:absolute;left:500px;top:52px;width:300px;color:var(--text-light);}
  .brand-name{display:flex;align-items:center;gap:12px;font-family:"Tinos",serif;font-weight:700;font-size:44px;line-height:1;}
  .brand-dot{width:34px;height:34px;border-radius:50%;background:var(--text-light);flex:none;}
  .centered{position:absolute;left:0;width:820px;text-align:center;margin:0;}
  .headline{top:446px;font-family:"Kaushan Script",cursive;font-weight:400;color:var(--sun);font-size:31px;line-height:44px;}
  .intro{top:540px;color:var(--text-light);font-size:15px;line-height:23px;}
  .tease{top:592px;font-family:"Kaushan Script",cursive;color:var(--sun);font-size:68px;line-height:90px;font-weight:400;}
  .launch-pill{position:absolute;left:141px;top:698px;width:538px;height:74px;border-radius:22px;
    background:linear-gradient(90deg,var(--sun) 0%,var(--sun-pale) 55%,var(--sun) 100%);
    color:var(--text-dark);font-size:21px;line-height:28px;text-align:center;display:flex;align-items:center;justify-content:center;}
  .launch-pill sup{font-size:11px;}
  .register{top:794px;color:var(--text-light);font-size:19px;line-height:30px;}
  .register strong{color:var(--sun);}
  .signup{position:absolute;left:0;top:870px;width:820px;height:290px;background:var(--paper);border-top:2px dotted var(--rule);color:var(--text-dark);}
  .signup-lead{position:absolute;left:46px;top:28px;width:700px;font-weight:700;font-size:17px;line-height:22px;margin:0;}
  .field{position:absolute;left:46px;width:430px;display:flex;align-items:flex-end;font-weight:700;font-size:19px;}
  .field-label{width:92px;}
  .field-line{flex:1;border-bottom:1px solid var(--rule);height:1px;margin-bottom:5px;}
  .optout{position:absolute;left:46px;top:228px;width:430px;font-size:14px;line-height:18px;margin:0;}
  .follow{position:absolute;left:580px;top:106px;width:200px;text-align:center;}
  .follow-title{font-size:24px;margin:0 0 24px;}
  .follow-list{display:flex;justify-content:center;gap:22px;font-size:15px;}
  .follow-item{display:flex;align-items:center;gap:6px;}
  .follow-dot{width:16px;height:16px;border-radius:50%;background:var(--ink);}
</style>
</head>
<body>
<main class="leaflet">
  <svg class="hero" viewBox="0 0 820 440" width="820" height="440">
    <defs>
      <linearGradient id="dine-tone" x1="0" y1="0" x2="1" y2="1">
        <stop offset="0" stop-color="var(--dine-green)"/>
        <stop offset="1" stop-color="var(--dine-warm)"/>
      </linearGradient>
      <linearGradient id="spa-tone" x1="0" y1="0" x2="1" y2="1">
        <stop offset="0" stop-color="#f3ece6"/>
        <stop offset="1" stop-color="var(--spa-soft)"/>
      </linearGradient>
      <polygon id="hex-cell" points="0,-86 73,-43 73,43 0,86 -73,43 -73,-43"/>
    </defs>
    <g role="img" aria-label="Photo of friends sharing an outdoor meal with wine among vineyards">
      <use href="#hex-cell" x="78" y="79" fill="url(#dine-tone)"/>
      <use href="#hex-cell" x="229" y="79" fill="url(#dine-tone)"/>
      <use href="#hex-cell" x="380" y="79" fill="url(#dine-tone)"/>
      <use href="#hex-cell" x="4" y="211" fill="url(#dine-tone)"/>
      <use href="#hex-cell" x="155" y="211" fill="url(#dine-tone)"/>
      <use href="#hex-cell" x="304" y="211" fill="url(#dine-tone)"/>
      <use href="#hex-cell" x="454" y="211" fill="url(#dine-tone)"/>
      <use href="#hex-cell" x="78" y="343" fill="url(#dine-tone)"/>
      <use href="#hex-cell" x="229" y="343" fill="url(#dine-tone)"/>
      <use href="#hex-cell" x="380" y="343" fill="url(#dine-tone)"/>
    </g>
    <g role="img" aria-label="Photo of a woman relaxing with a facial mask at a spa">
      <use href="#hex-cell" x="669" y="211" fill="url(#spa-tone)"/>
      <use href="#hex-cell" x="818" y="211" fill="url(#spa-tone)"/>
      <use href="#hex-cell" x="594" y="343" fill="url(#spa-tone)"/>
      <use href="#hex-cell" x="744" y="343" fill="url(#spa-tone)"/>
    </g>
  </svg>

  <div class="brand">
    <div class="brand-name"><span class="brand-dot"></span>Brindle Hub</div>
  </div>

  <h1 class="centered headline">Hey You!&nbsp; Want to win&nbsp; 200 to spend on the best<br>experiences the South West has to offer?</h1>
  <p class="centered intro">Brindle Hub is a brand spanking new website that gives you access to exciting offers<br>across the best restaurants, hotels, spas, leisure activities and services.</p>
  <p class="centered tease">Pretty cool?</p>

  <div class="launch-pill"><span>Launching on the <strong>1<sup>st</sup> August 2019</strong> – Be the first to<br>receive exclusive offers and WIN!</span></div>

  <p class="centered register">Register for free now at <strong>brindlehub.co.uk</strong> and find inspiration for places to <strong>EAT</strong>,<br>things to <strong>DO</strong> and where to get a <strong>PAMPER</strong>.</p>

  <section class="signup">
    <p class="signup-lead">Complete your details below for your chance to win and be the first to receive<br>fresh fancy offers just for you.</p>
    <div class="field" style="top:92px;"><span class="field-label">Name:</span><span class="field-line"></span></div>
    <div class="field" style="top:125px;"><span class="field-label">Email:</span><span class="field-line"></span></div>
    <div class="field" style="top:158px;"><span class="field-label">Mobile:</span><span class="field-line"></span></div>
    <div class="field" style="top:190px;"><span class="field-label">Address:</span><span class="field-line"></span></div>
    <p class="optout">( ) Please tick here if you would not like to receive updates on fabulous offers and new experiences.</p>
    <div class="follow">
      <p class="follow-title">Follow us</p>
      <div class="follow-list">
        <span class="follow-item"><span class="follow-dot"></span>Friendsy</span>
        <span class="follow-item"><span class="follow-dot"></span>Pictora</span>
      </div>
    </div>
  </section>
</main>
</body>
</html>
```